trifold brochure Bright Harbour

We need a new tri fold brochure (A4 folded to DL) for our company Bright Harbour Paramedical Services Pty Ltd. We have just had a new logo created and this is attached.

The main products we are wanting to highlight are:
1. First Aid training
2. Automated External Defibrillators (mainly the Pulsar Quick Link and Pulsar Quickcase AEDs)
3. First Aid Kits and Supplies

Our website is www.brightharb.com.au This website will be redeveloped in the near future,based on the design of the brochure.

We have added a lot of photos here, please feel free to use what you wish and alter as necessary.

Target Market(s)

Businesses, corporations, and sporting groups. We specialise in corporate courses and do very little public first aid training

Industry/Entity Type

Training

Requirements
Must have
• We are different to our main competitors in that all trainers are Professional Paramedics. Files that can be read and altered in Illustrator CS2 or InDesign CS2.
Nice to have
• A tag line - open to suggestions. Information about Sudden Cardiac Arrest (included in word doc)

```html
<!DOCTYPE html>
<html lang="en">
<head>
<meta charset="utf-8">
<title>Bright Harbour – Trifold Brochure Inside</title>
<link href="https://fonts.googleapis.com/css2?family=Arimo:ital,wght@0,400;0,700;1,400;1,700&family=Dancing+Script:wght@700&family=Tinos&display=swap" rel="stylesheet">
<style>
  :root{
    --red:#c8102e;
    --red-dark:#9e0c22;
    --ink:#3a3a3a;
    --grey-band:#d9d9d9;
    --grey-line:#bdbdbd;
    --paper:#ffffff;
    --page:#ffffff;
    --photo-skin:#d9b8a4;
    --photo-blue:#2f62a8;
    --photo-grey:#c9ccd0;
  }
  *{box-sizing:border-box;margin:0;padding:0}
  html,body{width:1200px;height:900px;overflow:hidden;background:var(--page)}
  body{font-family:"Arimo",Arial,sans-serif;color:var(--ink);position:relative}
  .sheet-label{
    position:absolute;top:26px;left:0;width:1200px;text-align:center;
    font-family:"Tinos","Times New Roman",serif;font-size:52px;color:#111;line-height:1;
  }
  .brochure{
    position:absolute;left:90px;top:110px;width:1060px;height:710px;
    background:var(--paper);border:1px solid #e3e3e3;
    display:grid;grid-template-columns:repeat(3,1fr);
  }
  .panel{position:relative;padding:58px 28px 0 28px;font-size:12.6px;line-height:1.28}
  .panel-header{position:absolute;left:0;top:14px;width:100%;height:34px}
  .panel-header .band{position:absolute;left:0;top:6px;right:0;height:22px;
    background:linear-gradient(#eeeeee,var(--grey-band));border-bottom:2px solid var(--grey-line)}
  .panel-header .tab{position:absolute;left:0;top:0;height:32px;padding:0 26px 0 22px;
    background:var(--red);border-radius:0 16px 0 0;color:#fff;
    font-family:"Dancing Script",cursive;font-size:21px;line-height:32px}
  .panel-header .mark{position:absolute;right:36px;top:2px;width:26px;height:26px;background:var(--red)}
  p{margin-bottom:12px}
  .course-title{color:var(--red);font-weight:700;font-style:italic;margin-bottom:1px}
  .script-heading{font-family:"Dancing Script",cursive;color:var(--red);font-size:20px;line-height:1;margin-bottom:2px}
  ul{list-style:none;margin-bottom:12px}
  li{padding-left:10px;position:relative}
  li::before{content:"•";position:absolute;left:0}
  .photo{position:absolute;display:block}
  .testimonial{position:absolute;left:0;top:570px;width:100%;height:140px}
  .testimonial .photo{left:0;top:0;width:140px;height:140px;
    background:linear-gradient(135deg,var(--photo-skin),#a0807a 60%,#5b5b63)}
  .quote{position:absolute;left:150px;top:6px;width:192px;color:var(--red);
    font-weight:700;font-style:italic;font-size:12px;line-height:1.25;text-align:center}
  .quote-by{display:block;color:var(--ink);font-weight:400;font-style:normal;font-size:10.5px;margin-top:6px}
  .kit-photo{left:40px;top:560px;width:280px;height:150px;border-radius:60px 60px 10px 10px;
    background:linear-gradient(#6d96cc,var(--photo-blue) 55%,#1d3f72)}
  .aed-photo{right:10px;top:580px;width:190px;height:130px;border-radius:14px;
    background:linear-gradient(135deg,#f2f2f2,var(--photo-grey) 60%,#8b8f96)}
  .aside-note{width:130px}
</style>
</head>
<body>
  <div class="sheet-label">inside</div>

  <main class="brochure">
    <!-- About panel -->
    <section class="panel panel-about">
      <div class="panel-header"><span class="band"></span><span class="tab">About Us</span><span class="mark"></span></div>
      <p>Bright Harbour Paramedical Services offers Nationally Accredited First Aid Courses.</p>
      <p>Our instructors are all Paramedics and accredited trainers. They have all performed CPR numerous times, including on the lounge room floor, defibrillated patients, managed victims of heart attack, and cared for the school child having an asthma attack.</p>
      <p>Our courses can be tailored to suit your business or we can develop a course specific to your needs.</p>
      <p>The certificate each participant receives is also recognised Australia wide.</p>
      <div class="script-heading">We also:</div>
      <ul>
        <li>develop tailored courses for business</li>
        <li>conduct training at your premises</li>
        <li>offer ongoing support to participants</li>
        <li>send out reaccreditation reminders</li>
        <li>monthly e-mail of First Aid updates</li>
      </ul>
      <div class="testimonial">
        <span class="photo" role="img" aria-label="Photo of a club doctor holding a defibrillator"></span>
        <p class="quote">“I would like to thank Bright Harbour for the tremendous support you have provided to the Elmcrest Football Club. Your advice &amp; assistance in supplying an AED was greatly appreciated, and the CPR and AED training session was outstanding…”
          <span class="quote-by">Dr Martin Hale<br>Consultant Paediatrician<br>Club Doctor Elmcrest<br>Football Club</span></p>
      </div>
    </section>

    <!-- Courses panel 1 -->
    <section class="panel panel-courses">
      <div class="panel-header"><span class="band"></span><span class="tab">Courses</span><span class="mark"></span></div>
      <div class="course-title">Perform CPR (HLTCPR201A)</div>
      <p>Participants gain the skills and knowledge required to perform Cardiopulmonary Resuscitation (CPR) in line with the National Resuscitation Council guidelines.</p>
      <div class="course-title">Basic Life Support (HLTFA201A)</div>
      <p>Frequently known as Level 1 First Aid, Participants are introduced to the skills and background knowledge required to recognise / respond to life threatening emergencies using basic life support techniques until a more qualified medically trained person is available.</p>
      <div class="course-title">Apply First Aid (HLTFA301B)</div>
      <p>Also frequently known as level 2 First Aid. This course represents the level of First Aid certification required by most industries and employers. Participants develop First Aid skills that may be applied in a range of situations, including community and workplace settings.</p>
      <p>This course can be delivered by flexible learning, reducing the time your employees are out of the office.</p>
      <span class="photo kit-photo" role="img" aria-label="Photo of a blue first response kit bag with an AED"></span>
    </section>

    <!-- Courses panel 2 -->
    <section class="panel panel-courses">
      <div class="panel-header"><span class="band"></span><span class="tab">Courses</span><span class="mark"></span></div>
      <div class="course-title">Automated External Defibrillation (21658VIC)</div>
      <p>Participants develop the necessary skills to safely and effectively resuscitate a patient in cardiac arrest using a Automated External Defibrillator and Cardiopulmonary Resuscitation in line with the National Resuscitation Council guidelines.</p>
      <div class="course-title">First Aid Management Of Anaphylaxis (21659VIC)</div>
      <p style="margin-bottom:0">Participants develop the skills and knowledge to provide first aid to a patient suffering from anaphylaxis. Course includes:</p>
      <ul>
        <li>Anaphylaxis Risk Minimisation</li>
        <li>Anaphylaxis Management Plans</li>
        <li>Recognition &amp; Treatment of Anaphylaxis</li>
        <li>Use of EpiShot or AnaDose</li>
      </ul>
      <div class="course-title">First Aid For Parents</div>
      <p style="margin-bottom:0">A brief course encompassing all the “must know” elements of first aid for the parents of infants and toddlers. Includes:</p>
      <ul>
        <li>CPR for babies &amp; children</li>
        <li>Choking</li>
        <li>Short of Breath (Asthma, Croup)</li>
      </ul>
      <p class="aside-note">Designed to fit into the busy schedule of new mums &amp; dads, whilst not breaking their budget.</p>
      <span class="photo aed-photo" role="img" aria-label="Photo of a defibrillator unit and a pen"></span>
    </section>
  </main>
</body>
</html>
```